Clean, professional business cards for successful realtor

I want a clean and professional business card designed that successfully brands myself.
I want to be able to change the headshot, if possible. A white background instead of the brick would be great!
Please put this quote on the back of the card under the kov logo, "Ask me about my Step-Ahead program!"

Target Market(s)

Home buyers and sellers

Industry/Entity Type

Real Estate Agent

Contact Information for Business Card

Professional and Clean.

Font styles to use
Serif
Decorative
Script

Requirements
Must have
• Marlene Quist - Realtor
• Direct: 555.304.2296
• MarlSellsSA@postvane.com
• www.marlenequist.sa.kovrealty.com
Nice to have
• Lighter colors, white and crisp would be nice.
• I would prefer my photo on the front of the card

```html
<!DOCTYPE html>
<html lang="en">
<head>
<meta charset="utf-8">
<title>Marlene Quist – Realtor Business Card</title>
<link rel="stylesheet" href="https://fonts.googleapis.com/css2?family=Montserrat:wght@400;600&family=Pacifico&family=Yesteryear&display=swap">
<style>
  :root {
    --teal: #0599ae;
    --teal-deep: #058a9e;
    --white: #ffffff;
    --navy: #1b2f7a;
    --backdrop: #d4d4d4;
    --photo-tone: linear-gradient(135deg, #9b6b4e 0%, #c49a82 45%, #6b4536 100%);
  }
  * { box-sizing: border-box; margin: 0; padding: 0; }
  html, body {
    width: 1200px; height: 1200px; overflow: hidden;
    background: var(--backdrop);
    font-family: "Montserrat", Arial, sans-serif;
  }
  .sheet {
    position: relative; width: 1200px; height: 1200px;
    display: flex; flex-direction: column; align-items: center; justify-content: center; gap: 52px;
  }
  .card {
    position: relative; width: 900px; height: 514px; overflow: hidden;
    box-shadow: 0 6px 18px rgba(0,0,0,0.18);
  }

  /* Front */
  .card-front { background: var(--teal); }
  .front-band {
    position: absolute; left: 230px; top: 0; width: 670px; height: 165px;
    background: var(--white);
  }
  .house-mark { position: absolute; left: 40px; top: 150px; width: 150px; height: 130px; }
  .headshot {
    position: absolute; left: 215px; top: 55px; width: 190px; height: 190px;
    border-radius: 50%; border: 6px solid var(--white);
    background: var(--photo-tone);
  }
  .brand {
    display: flex; align-items: center; gap: 12px;
    font-weight: 600; color: var(--navy); letter-spacing: 1px;
  }
  .card-front .brand { position: absolute; right: 60px; top: 62px; font-size: 40px; }
  .brand-square { width: 36px; height: 36px; background: var(--navy); }
  .agent-name {
    position: absolute; left: 330px; top: 185px; width: 520px; text-align: center;
    font-family: "Pacifico", cursive; font-size: 62px; color: var(--white); line-height: 1.2;
  }
  .agent-title {
    position: absolute; left: 330px; top: 285px; width: 520px; text-align: center;
    font-size: 24px; color: var(--white); letter-spacing: 2px;
  }
  .contact {
    position: absolute; left: 120px; top: 330px;
    display: flex; flex-direction: column; gap: 12px;
    color: var(--white); font-size: 25px;
  }
  .contact-line { display: flex; align-items: center; gap: 18px; }
  .contact-line svg { width: 28px; height: 28px; flex: none; }

  /* Back */
  .card-back { background: var(--white); }
  .quote-band {
    position: absolute; left: 0; top: 90px; width: 900px; height: 270px;
    background: var(--teal);
    display: flex; align-items: center; justify-content: center;
  }
  .quote {
    font-family: "Yesteryear", cursive; font-size: 40px; line-height: 1.3;
    color: var(--white); text-align: center; width: 760px;
  }
  .back-footer {
    position: absolute; left: 0; top: 360px; width: 900px; height: 154px;
    display: flex; flex-direction: column; align-items: center; justify-content: center; gap: 12px;
  }
  .card-back .brand { font-size: 34px; }
  .card-back .brand-square { width: 30px; height: 30px; }
  .program-note { font-size: 22px; color: var(--teal-deep); letter-spacing: 0.5px; }
</style>
</head>
<body>
<main class="sheet">
  <section class="card card-front" aria-label="Business card front">
    <div class="front-band"></div>
    <svg class="house-mark" viewBox="0 0 150 130" aria-hidden="true">
      <path d="M75 10 L140 60 L120 60 L120 125 L90 125 L90 80 L60 80 L60 125 L30 125 L30 60 L10 60 Z" fill="var(--teal-deep)"/>
    </svg>
    <div class="headshot" role="img" aria-label="Headshot of Marlene Quist on a white background"></div>
    <div class="brand"><span class="brand-square"></span><span>kov realty</span></div>
    <h1 class="agent-name">Marlene Quist</h1>
    <p class="agent-title">REALTOR</p>
    <div class="contact">
      <div class="contact-line">
        <svg viewBox="0 0 24 24" aria-hidden="true"><path fill="#fff" d="M6.6 10.8a15.1 15.1 0 0 0 6.6 6.6l2.2-2.2a1 1 0 0 1 1-.25 11.4 11.4 0 0 0 3.6.57 1 1 0 0 1 1 1V20a1 1 0 0 1-1 1A17 17 0 0 1 3 4a1 1 0 0 1 1-1h3.5a1 1 0 0 1 1 1c0 1.25.2 2.45.57 3.57a1 1 0 0 1-.25 1z"/></svg>
        <span>Direct: 555.304.2296</span>
      </div>
      <div class="contact-line">
        <svg viewBox="0 0 24 24" aria-hidden="true"><rect x="2" y="5" width="20" height="14" fill="#fff"/><path d="M2 5 L12 13 L22 5" stroke="var(--teal)" stroke-width="1.6" fill="none"/></svg>
        <span>MarlSellsSA@postvane.com</span>
      </div>
      <div class="contact-line">
        <svg viewBox="0 0 24 24" aria-hidden="true"><circle cx="12" cy="12" r="9" fill="none" stroke="#fff" stroke-width="1.8"/><path d="M3 12h18M12 3c3 3 3 15 0 18M12 3c-3 3-3 15 0 18" fill="none" stroke="#fff" stroke-width="1.4"/></svg>
        <span>www.marlenequist.sa.kovrealty.com</span>
      </div>
    </div>
  </section>

  <section class="card card-back" aria-label="Business card back">
    <div class="quote-band">
      <p class="quote">"The referral of your family and friends is the greatest compliment you can give me, thank you for your trust."</p>
    </div>
    <div class="back-footer">
      <div class="brand"><span class="brand-square"></span><span>kov realty</span></div>
      <p class="program-note">Ask me about my Step-Ahead program!</p>
    </div>
  </section>
</main>
</body>
</html>
```